Webdesign für islamisches Bestattungsunternehmen
Zielgruppe
islamisches Bestattungsunternehmen, Grabsteine, Grabpflege
Aufgabenstellung
wir wollen ein elegantes design mit einem hauch an exklusivität. wir sind nicht auf billig aus, tatsächlich hochwertig, etwas teurer als die konkurrenz aber dafür bieten wir auch was an.
unser logo haben wir auch hier machen lassen.
www.nur-samira.eu
LEUTE!
Wir wünschen uns dass direkt auf der ersten seite die 3 optionen sofort ersichtlich sind!!! nicht dass die leute noch runterscrollen müssen...

```html
<!DOCTYPE html>
<html lang="de">
<head>
<meta charset="utf-8">
<title>Nur-Samira – Islamische Bestattungen</title>
<link href="https://fonts.googleapis.com/css2?family=Lato:wght@400;700;900&display=swap" rel="stylesheet">
<style>
:root{
  --bg:#e9d9c5;
  --card:#eee2d3;
  --panel:#ebdccb;
  --brown-dark:#6e4119;
  --brown:#8c5a2c;
  --brown-light:#b07640;
  --heading:#7a4a22;
  --tab:#b98a62;
  --text:#3a2a1c;
  --field:#f3f1ee;
  --red:#d71a1a;
  --white:#ffffff;
}
*{box-sizing:border-box;margin:0;padding:0}
html,body{width:1200px;height:3151px;overflow:hidden}
body{background:var(--bg);font-family:'Lato',sans-serif;color:var(--text);position:relative}
.abs{position:absolute}
.site-header{left:0;top:0;width:1200px;height:76px;background:linear-gradient(#9b6330,#7d4f22);border-bottom:3px solid #5a3514}
.brand{display:flex;align-items:center;gap:8px;color:var(--white);font-weight:900;font-size:15px;letter-spacing:1px}
.brand-dot{width:14px;height:14px;border-radius:50%;background:var(--white)}
.site-header .brand{position:absolute;left:150px;top:28px}
.main-nav{position:absolute;left:510px;top:28px;display:flex}
.main-nav a{color:var(--white);text-decoration:none;font-size:12px;font-weight:700;letter-spacing:1px;margin-right:38px}
.hero{left:0;top:76px;width:1200px;height:386px;display:flex}
.hero-photo{height:100%}
.hero-title{left:0;top:282px;width:1200px;text-align:center;color:var(--white);font-size:31px;font-weight:700;text-shadow:0 2px 4px rgba(0,0,0,.7)}
.service-btn{height:51px;width:252px;background:linear-gradient(#a9692f,#7a4618);border:2px solid #d8b58c;color:var(--white);font-size:21px;font-weight:700;display:flex;align-items:center;justify-content:center;box-shadow:0 4px 6px rgba(0,0,0,.35);top:438px}
.section-title{color:var(--heading);font-weight:700;font-size:22px;letter-spacing:1px}
.body-copy{font-size:11.5px;line-height:19px}
.about-image{left:196px;top:563px;width:263px;height:226px;background:radial-gradient(#f0ebe5,#cbc3ba);border-radius:40% 40% 10% 10%}
.tab{top:824px;height:44px;width:212px;display:flex;align-items:center;justify-content:center;font-size:15px;color:var(--white);background:var(--tab)}
.tab.active{background:#eadcca;color:var(--heading)}
.panel{left:187px;top:870px;width:826px;height:610px;background:var(--panel);border:1px solid #d2bda4}
.gallery{left:219px;top:900px;width:767px;height:490px;display:grid;grid-template-rows:1fr 1fr;gap:2px}
.gallery-row{display:flex;gap:2px}
.gallery-row div{flex:1}
.form-btn{left:494px;top:1415px;width:212px;height:41px;background:var(--brown-light);color:var(--white);font-size:14px;display:flex;align-items:center;justify-content:center;gap:8px;box-shadow:0 2px 3px rgba(0,0,0,.3)}
.prayer-card{top:1574px;width:243px;height:255px;background:var(--card);padding:22px 20px;box-shadow:0 12px 10px -8px rgba(0,0,0,.35)}
.prayer-card h3{color:var(--brown);font-size:14.5px;font-weight:700;margin-bottom:14px}
.prayer-card p{font-size:11px;line-height:15px;margin-bottom:14px}
.prayer-card .more{color:var(--brown);font-size:11px}
.prayer-flowers{position:absolute;left:30px;bottom:-12px;width:183px;height:34px;background:linear-gradient(90deg,#f2c9cf,#f7e8e2,#eab8c0,#f7e8e2,#f2c9cf);border-radius:20px}
.arrow-btn{width:28px;height:28px;border:1.5px solid #5a4030;border-radius:50%;top:1683px}
.manager-photo{left:767px;top:1903px;width:243px;height:278px;background:#efe3d5;padding:12px}
.manager-photo div{width:100%;height:100%;background:linear-gradient(#7e9a6a,#4a5640 60%,#6f7d5a)}
.review-card{top:2286px;height:218px;background:var(--card);padding:30px 34px;font-size:11.5px;line-height:15px}
.review-card p{margin-bottom:15px}
.stars{color:var(--brown-dark);font-size:15px;letter-spacing:1px}
.dots{left:566px;top:2526px;display:flex;gap:7px}
.dots span{width:8px;height:8px;border-radius:50%;border:1.5px solid #5a4030}
.dots span.on{background:#5a4030}
.field{background:var(--field);height:39px;font-size:11.5px;color:#6a5a4e;padding:0 18px;display:flex;align-items:center;border:1px solid #ddd}
.send-btn{left:646px;top:2860px;width:242px;height:38px;background:#b0693a;color:var(--white);font-weight:700;font-size:14px;letter-spacing:2px;display:flex;align-items:center;justify-content:center}
.catalog-band{left:150px;top:2960px;width:900px;height:114px;background:linear-gradient(90deg,#fffdf9,#f3ebe1)}
.pdf-btn{left:192px;top:2988px;width:320px;height:62px;background:var(--red);border:2px solid #8d0d0d;color:var(--white);font-size:21px;font-weight:700;display:flex;align-items:center;gap:20px;padding-left:28px;box-shadow:0 3px 5px rgba(0,0,0,.3)}
.banner-slogan{left:620px;top:2992px;width:280px;color:#a66a35;font-size:20px;font-weight:700;line-height:26px;white-space:nowrap}
.site-footer{left:0;top:3074px;width:1200px;height:77px;background:linear-gradient(#8a5a2b,#6e4119)}
.site-footer a,.site-footer span{color:var(--white);font-size:11px;text-decoration:none}
</style>
</head>
<body>

<header class="site-header abs">
  <div class="brand"><span class="brand-dot"></span>NUR-SAMIRA</div>
  <nav class="main-nav">
    <a>STARTSEITE</a><a>BESTATTUNG</a><a>GRABSTEINE</a><a>GRABPFLEGE</a><a>KONTAKT</a>
  </nav>
</header>

<section class="hero abs">
  <div class="hero-photo" role="img" aria-label="Grab mit weißem Marmorgrabstein" style="width:164px;background:linear-gradient(#6d7a52,#9a958a)"></div>
  <div class="hero-photo" role="img" aria-label="Gepflegtes Grab mit dunklem Grabstein im Grünen" style="width:291px;background:linear-gradient(#6f8a4c,#6a6a62 60%,#8b7d6c)"></div>
  <div class="hero-photo" role="img" aria-label="Roter Granitgrabstein auf Friedhof" style="width:292px;background:linear-gradient(#585a55,#a04a58 50%,#6a5a48)"></div>
  <div class="hero-photo" role="img" aria-label="Trauernde Frau mit Blumenkranz" style="width:293px;background:linear-gradient(90deg,#3a3430,#c8b9a8 60%,#e4d8ce)"></div>
  <div class="hero-photo" role="img" aria-label="Weißer Grabstein mit Blumen" style="width:160px;background:linear-gradient(#c9d0d6,#7d8288)"></div>
</section>
<h1 class="hero-title abs">Bestattungen deutschlandweit, Überführungen weltweit</h1>
<div class="service-btn abs" style="left:181px">GRABPFLEGE</div>
<div class="service-btn abs" style="left:476px">GRABSTEINE</div>
<div class="service-btn abs" style="left:767px">BESTATTUNG</div>

<svg class="abs" style="left:150px;top:500px" width="902" height="62" viewBox="0 0 902 62">
  <path d="M0 48 C300 30 600 10 820 8 C870 8 900 20 900 60" fill="none" stroke="#7d4f22" stroke-width="3"/>
</svg>

<div class="about-image abs" role="img" aria-label="Herzförmiger Marmorgrabstein mit Engelsfigur"></div>
<h2 class="section-title abs" style="left:500px;top:594px">WER WIR SIND</h2>
<p class="body-copy abs" style="left:500px;top:642px;width:502px">Lorem ipsum dolor sit amet, consectetur adipiscing elit, sed do eiusmod tempor incididunt ut labore et dolore magna aliqua. Ut enim ad minim veniam, quis nostrud exercitation ullamco laboris nisi ut aliquip ex ea commodo consequat. Duis aute irure dolor in reprehenderit in voluptate velit esse cillum dolore eu fugiat nulla pariatur. Excepteur sint occaecat cupidatat non proident, sunt in culpa qui officia deserunt mollit anim id est laborum.</p>

<div class="tab active abs" style="left:273px">Grabpflege</div>
<div class="tab abs" style="left:494px">Grabsteine</div>
<div class="tab abs" style="left:714px">Bestattung</div>
<div class="panel abs"></div>
<div class="gallery abs" role="img" aria-label="Fotogalerie gepflegter Gräber">
  <div class="gallery-row">
    <div style="background:linear-gradient(#4a4d55,#6a6f80)"></div>
    <div style="background:linear-gradient(#6a8a48,#a9876a)"></div>
    <div style="background:linear-gradient(#6e6650,#c9b48f)"></div>
    <div style="background:linear-gradient(#7a9a58,#8a8c92)"></div>
  </div>
  <div class="gallery-row">
    <div style="background:linear-gradient(#7a9a58,#8a8c92)"></div>
    <div style="background:linear-gradient(#6e6650,#c9b48f)"></div>
    <div style="background:linear-gradient(#6a8a48,#a9876a)"></div>
    <div style="background:linear-gradient(#4a4d55,#6a6f80)"></div>
  </div>
</div>
<div class="form-btn abs">
  <svg width="18" height="18" viewBox="0 0 18 18"><rect x="2" y="1" width="12" height="16" fill="none" stroke="#fff" stroke-width="1.5"/><path d="M5 6h6M5 9h6M5 12h4" stroke="#fff" stroke-width="1.5"/></svg>
  Formular Herunterladen
</div>

<h2 class="section-title abs" style="left:0;width:1200px;text-align:center;top:1520px">GEBETE</h2>
<svg class="arrow-btn abs" style="left:165px" viewBox="0 0 28 28"><path d="M16 8l-6 6 6 6" fill="none" stroke="#5a4030" stroke-width="1.5"/></svg>
<svg class="arrow-btn abs" style="left:1006px" viewBox="0 0 28 28"><path d="M12 8l6 6-6 6" fill="none" stroke="#5a4030" stroke-width="1.5"/></svg>
<article class="prayer-card abs" style="left:217px">
  <h3>Gebet von Fatima Zahraa (ع) I</h3>
  <p>Es ist auch als „Namaz des Istighaatha“, eine Bitte, bekannt. Es ist ein 2 Rakaa Gebet und wird genau wie das Morgengebet vollzogen.</p>
  <p>Rezitiere nach dem Salam, das Salawat (Allahumma salli ala Muhammad wa aali Muhammad), Bismilahi Rahmani..</p>
  <span class="more">Mehr...</span>
  <div class="prayer-flowers" role="img" aria-label="Rosenranke"></div>
</article>
<article class="prayer-card abs" style="left:482px">
  <h3>Gebet von Fatima Zahraa (ع) I</h3>
  <p>Es ist auch als „Namaz des Istighaatha“, eine Bitte, bekannt. Es ist ein 2 Rakaa Gebet und wird genau wie das Morgengebet vollzogen.</p>
  <p>Rezitiere nach dem Salam, das Salawat (Allahumma salli ala Muhammad wa aali Muhammad), Bismilahi Rahmani..</p>
  <span class="more">Mehr...</span>
  <div class="prayer-flowers" role="img" aria-label="Rosenranke"></div>
</article>
<article class="prayer-card abs" style="left:745px">
  <h3>Gebet von Fatima Zahraa (ع) I</h3>
  <p>Es ist auch als „Namaz des Istighaatha“, eine Bitte, bekannt. Es ist ein 2 Rakaa Gebet und wird genau wie das Morgengebet vollzogen.</p>
  <p>Rezitiere nach dem Salam, das Salawat (Allahumma salli ala Muhammad wa aali Muhammad), Bismilahi Rahmani..</p>
  <span class="more">Mehr...</span>
  <div class="prayer-flowers" role="img" aria-label="Rosenranke"></div>
</article>

<p class="abs" style="left:188px;top:1914px;font-size:14px">Der Geschäftsführer</p>
<h2 class="section-title abs" style="left:188px;top:1932px">HIER BENENNEN</h2>
<div class="body-copy abs" style="left:188px;top:1972px;width:542px">
  <p style="margin-bottom:19px">Lorem ipsum dolor sit amet, consectetur adipiscing elit, sed do eiusmod tempor incididunt ut labore et dolore magna aliqua. Ut enim ad minim veniam, quis nostrud exercitation ullamco laboris nisi ut aliquip ex ea commodo consequat. Duis aute irure dolor in reprehenderit in voluptate velit esse cillum dolore eu fugiat nulla pariatur. Excepteur sint occaecat cupidatat non proident, sunt in culpa qui officia deserunt mollit anim id est laborum.</p>
  <p>Ut enim ad minim veniam, quis nostrud exercitation ullamco laboris nisi ut aliquip ex ea commodo consequat. Duis aute irure dolor in reprehenderit in voluptate velit esse cillum dolore eu fugiat nulla pariatur. Excepteur sint occaecat cupidatat non proident, sunt in culpa qui officia deserunt mollit anim.</p>
</div>
<div class="manager-photo abs"><div role="img" aria-label="Porträt des Geschäftsführers im dunklen Hemd an einer Landstraße"></div></div>

<div class="abs" role="img" aria-label="Bewertungsgrafik mit fünf Sternen" style="left:187px;top:2196px;width:180px;height:91px;background:linear-gradient(90deg,#e2d3bf,#ead9c6);border-radius:6px"></div>
<h2 class="section-title abs" style="left:471px;top:2237px">REZENSIO-BEWERTUNGEN</h2>
<article class="review-card abs" style="left:185px;width:409px">
  <p>Lorem ipsum dolor sit amet, consectetur adipiscing elit, sed do eiusmod tempor incididunt ut labore et dolore magna aliqua. Ut enim ad minim veniam, quis nostrud exercitation ullamco laboris nisi ut aliquip ex ea commodo consequat.</p>
  <p>Ut enim ad minim veniam, quis nostrud exercitation ullamco laboris nisi ut aliquip ex ea commodo consequat.</p>
  <div class="stars">★★★★★</div>
  <div style="margin-top:6px">Lena Hartwig</div>
</article>
<article class="review-card abs" style="left:613px;width:399px">
  <p>Lorem ipsum dolor sit amet, consectetur adipiscing elit, sed do eiusmod tempor incididunt ut labore et dolore magna aliqua. Ut enim ad minim veniam, quis nostrud exercitation ullamco laboris nisi ut aliquip ex ea commodo consequat.</p>
  <p>Ut enim ad minim veniam, quis nostrud exercitation ullamco laboris nisi ut aliquip ex ea commodo consequat.</p>
  <div class="stars">★★★★★</div>
  <div style="margin-top:6px">Lena Hartwig</div>
</article>
<div class="dots abs"><span class="on"></span><span></span><span></span><span></span><span></span></div>

<div class="abs" role="img" aria-label="Grabanlage mit dunklem Grabstein und Kiesbett" style="left:245px;top:2566px;width:223px;height:321px;background:linear-gradient(#4a423c,#a8a196 50%,#6f6b66);border-radius:4px"></div>
<h2 class="abs" style="left:712px;top:2600px;color:var(--brown);font-size:22px;font-weight:700">Title Here</h2>
<div class="field abs" style="left:511px;top:2648px;width:244px">Name</div>
<div class="field abs" style="left:769px;top:2648px;width:244px">Email</div>
<div class="field abs" style="left:511px;top:2701px;width:244px;justify-content:space-between">Bestattung
  <svg width="12" height="8" viewBox="0 0 12 8"><path d="M0 0h12L6 8z" fill="#7a5a45"/></svg></div>
<div class="field abs" style="left:771px;top:2701px;width:244px;padding-right:3px;justify-content:space-between">Datei-Upload
  <span style="background:#b0693a;color:#fff;font-weight:700;padding:8px 12px">Durchsuche</span></div>
<div class="field abs" style="left:511px;top:2755px;width:505px;height:89px;align-items:flex-start;padding-top:12px">Kommentare</div>
<div class="send-btn abs">SENDEN</div>

<div class="catalog-band abs"></div>
<div class="pdf-btn abs">
  <svg width="34" height="40" viewBox="0 0 34 40"><rect x="1" y="1" width="32" height="38" fill="#fff"/><rect x="1" y="1" width="16" height="9" fill="#b00"/><path d="M8 30h18M8 24h18" stroke="#b00" stroke-width="2"/></svg>
  Katalog Herunterladen
</div>
<svg class="abs" style="left:570px;top:2962px" width="2" height="110"><line x1="1" y1="0" x2="1" y2="110" stroke="#9a7a5a" stroke-dasharray="4 3"/></svg>
<p class="banner-slogan abs">Bestattungen deutschlandweit,<br>Überführungen weltweit</p>
<div class="abs" role="img" aria-label="Flugzeug und weißer Wagen für Überführungen" style="left:912px;top:2974px;width:136px;height:96px;background:linear-gradient(135deg,#eeeef0,#cfd1d6);border-radius:4px"></div>

<footer class="site-footer abs">
  <div class="brand" style="position:absolute;left:150px;top:30px">
    <span class="brand-dot"></span>NUR-SAMIRA</div>
  <div style="position:absolute;left:474px;top:32px">
    <a>Datenschutzerklärung</a><span> &nbsp;|&nbsp; </span><a>Haftung</a><span> &nbsp;|&nbsp; </span><a>Impressum</a>
  </div>
  <span style="position:absolute;left:896px;top:32px">Copyright Nur-Samira.eu © 2021</span>
</footer>

</body>
</html>
```